Post storm repair flyer

looking for an eye catching 6x9 postcard to send out to single family home owners advertising a "Post Storm Repair Special" explaining that after the recent hurricanes its very important to have your roof checked and any repairs fixed right away before they become a bigger more costly problem and that even though your home wasn't directly hit by the storm the high wind gust could've cause unseen damage.
offer $200 off any repair *some rules may apply
Lark Roofing
888.417.LARK
www.LarkRoofing.example

Roofing

```html
<!DOCTYPE html>
<html lang="en">
<head>
<meta charset="utf-8">
<title>Lark Roofing – Post Storm Repair Special Postcard</title>
<link href="https://fonts.googleapis.com/css2?family=League+Gothic&family=Montserrat:wght@500;600&family=Poppins:wght@800&family=Roboto+Condensed:wght@400;700&display=swap" rel="stylesheet">
<style>
  :root {
    --backdrop: #3a2a08;
    --gold: #e6ae22;
    --ink: #0d0d0d;
    --paper: #ffffff;
    --shade: #262523;
  }
  * { margin: 0; padding: 0; box-sizing: border-box; }
  html, body { width: 1200px; height: 1200px; overflow: hidden; }
  body { background: var(--backdrop); position: relative; font-family: "Roboto Condensed", sans-serif; }

  .postcard { position: absolute; left: 194px; width: 787px; height: 525px; overflow: hidden; background: var(--paper); }
  .postcard--front { top: 45px; }
  .postcard--back { top: 630px; }
  .postcard svg.shapes { position: absolute; inset: 0; width: 787px; height: 525px; }

  .brand-name { position: absolute; font-family: "Montserrat", sans-serif; font-weight: 500; white-space: nowrap; text-align: center; }
  .front-brand { left: 22px; top: 120px; width: 170px; font-size: 13px; color: var(--ink); }

  .headline { position: absolute; left: 26px; top: 188px; font-family: "League Gothic", sans-serif; font-weight: 400; font-size: 48px; line-height: 52px; color: var(--paper); text-transform: uppercase; white-space: nowrap; }

  .storm-copy { position: absolute; left: 32px; top: 320px; font-size: 15px; line-height: 16px; color: var(--ink); white-space: nowrap; }

  .back-brand { left: 101px; top: 134px; width: 200px; font-size: 13px; color: var(--paper); }
  .offer { position: absolute; left: 0; width: 396px; text-align: center; color: var(--paper); }
  .offer-label { top: 180px; font-family: "Poppins", sans-serif; font-weight: 800; font-size: 60px; letter-spacing: -1px; line-height: 80px; }
  .offer-amount { top: 268px; font-family: "League Gothic", sans-serif; font-size: 76px; line-height: 76px; }
  .offer-scope { top: 336px; font-family: "League Gothic", sans-serif; font-size: 68px; line-height: 68px; }
  .offer-scope sup { font-family: "Roboto Condensed", sans-serif; font-size: 30px; vertical-align: 26px; margin-left: 6px; }
  .offer-terms { top: 414px; font-size: 22px; line-height: 28px; }

  .stamp-box { position: absolute; left: 600px; top: 66px; width: 123px; height: 154px; border: 1.5px solid var(--ink); }
  .address-line { position: absolute; left: 512px; width: 210px; height: 0; border-top: 1.5px solid var(--ink); }

  .footer-brand { left: 462px; top: 487px; width: 110px; font-size: 7.5px; color: var(--ink); }
  .footer-mark { position: absolute; left: 505px; top: 466px; width: 16px; height: 16px; border: 1.5px solid var(--ink); border-radius: 50%; }
  .contact { position: absolute; left: 609px; font-family: "Roboto Condensed", sans-serif; font-weight: 700; font-size: 15px; color: var(--ink); white-space: nowrap; }
  .contact-phone { top: 442px; }
  .contact-web { top: 472px; }
  .contact-icon { position: absolute; left: 586px; top: 474px; width: 14px; height: 14px; }
</style>
</head>
<body>

<section class="postcard postcard--front" aria-label="Postcard front">
  <svg class="shapes" viewBox="0 0 787 525">
    <defs>
      <linearGradient id="roofPhoto" x1="0" y1="0" x2="0" y2="1">
        <stop offset="0" stop-color="#c9dcef"/>
        <stop offset="0.45" stop-color="#a9b9c6"/>
        <stop offset="0.6" stop-color="#5d5e60"/>
        <stop offset="1" stop-color="#8a7a66"/>
      </linearGradient>
    </defs>
    <polygon class="hex-top" points="190,27 218,0 294,0 320,27 290,81 220,81" fill="#0d0d0d"/>
    <polygon class="hex-accent" points="282,187 350,67 446,67 366,203 330,267" fill="#e6ae22"/>
    <polygon class="title-banner" points="0,175 216,175 277,301 0,301" fill="#e6ae22"/>
    <polygon class="base-band" points="0,494 310,494 290,525 0,525" fill="#e6ae22"/>
    <polygon class="divider" points="458,0 502,0 378,231 338,427 426,525 394,525 290,443 326,231" fill="#0d0d0d"/>
    <polygon class="photo" role="img" aria-label="Photo of two roofers inspecting a shingle roof on a brick house" points="502,0 787,0 787,525 426,525 338,427 378,231" fill="url(#roofPhoto)"/>
    <polygon class="hex-corner" points="672,39 694,0 787,0 787,110 710,110" fill="#0d0d0d"/>
    <polygon class="hex-bottom" points="574,525 602,474 666,474 694,525" fill="#e6ae22"/>
  </svg>

  <div class="brand-name front-brand">LARKROOFING.EXAMPLE</div>
  <h1 class="headline">Post Storm<br>Repair Special</h1>
  <p class="storm-copy">Explaining that after the recent<br>hurricanes its very important to<br>have your roof checked and any<br>repairs fixed right away before<br>they become a bigger more costly<br>problem and that even though<br>your home wasn't directly hit by<br>the storm the high wind gust<br>could've cause unseen damage.</p>
</section>

<section class="postcard postcard--back" aria-label="Postcard back">
  <svg class="shapes" viewBox="0 0 787 525">
    <defs>
      <linearGradient id="darkPhoto" x1="0" y1="0" x2="0" y2="1">
        <stop offset="0" stop-color="#3a3b36"/>
        <stop offset="0.5" stop-color="#2a2927"/>
        <stop offset="1" stop-color="#1f1e1d"/>
      </linearGradient>
    </defs>
    <polygon class="photo" role="img" aria-label="Darkened photo of a roofer working on a shingle roof" points="0,0 490,0 390,525 0,525" fill="url(#darkPhoto)"/>
    <polygon class="divider" points="490,0 508,0 410,525 390,525" fill="#e6ae22"/>
  </svg>

  <div class="brand-name back-brand">LARKROOFING.EXAMPLE</div>
  <div class="offer offer-label">OFFER</div>
  <div class="offer offer-amount">$200 OFF</div>
  <div class="offer offer-scope">ANY REPAIR<sup>*</sup></div>
  <div class="offer offer-terms">(some rules may apply)</div>

  <div class="stamp-box"></div>
  <div class="address-line" style="top:288px"></div>
  <div class="address-line" style="top:330px"></div>
  <div class="address-line" style="top:369px"></div>
  <div class="address-line" style="top:402px"></div>

  <div class="footer-mark"></div>
  <div class="brand-name footer-brand">LARKROOFING.EXAMPLE</div>
  <div class="contact contact-phone">888.417.LARK</div>
  <svg class="contact-icon" viewBox="0 0 14 14" aria-hidden="true">
    <circle cx="7" cy="7" r="6" fill="none" stroke="#0d0d0d" stroke-width="1.4"/>
    <ellipse cx="7" cy="7" rx="2.6" ry="6" fill="none" stroke="#0d0d0d" stroke-width="1.2"/>
    <line x1="1" y1="7" x2="13" y2="7" stroke="#0d0d0d" stroke-width="1.2"/>
  </svg>
  <div class="contact contact-web">www.LarkRoofing.example</div>
</section>

</body>
</html>
```